Fabric Softener

We need fabric softener. Bottle picture attached for reference. Color of bottle can be proposed as well. Normally bottle is pink and blue color

Logo is also attached that shall be used.
Updates

Need extra days to review

Low designer entries

Target Market(s)

Niche

Font styles to use
Sans Serif

Requirements
Must have
• Fabric, Brightness, Nature
Nice to have
• Good colors
Should not have
• Adults

```html
<!DOCTYPE html>
<html lang="en">
<head>
<meta charset="utf-8">
<title>Lumera Ultra Fabric Softener – Label</title>
<link rel="stylesheet" href="https://fonts.googleapis.com/css2?family=Alfa+Slab+One&family=Grenze:wght@600&family=Oswald:wght@500&family=Work+Sans:wght@400;800&family=Baloo+2:wght@800&display=swap">
<style>
  :root {
    --page: #f1f1f3;
    --sky-top: #d7f0fd;
    --sky-mid: #8fd3f6;
    --sky-deep: #3fb1e8;
    --navy: #241a5f;
    --magenta: #c8076f;
    --purple: #6f5ba8;
    --gold: #e6b12c;
    --gold-deep: #b9801a;
    --white: #ffffff;
    --ink: #2c2a55;
  }
  * { box-sizing: border-box; margin: 0; padding: 0; }
  html, body { width: 1124px; height: 1200px; overflow: hidden; background: var(--page); }
  body { position: relative; font-family: "Work Sans", sans-serif; color: var(--ink); }

  .label {
    position: absolute; left: 112px; top: 60px; width: 900px; height: 1080px;
    border-radius: 360px 48px 48px 48px; overflow: hidden;
  }
  .label-backdrop {
    position: absolute; inset: 0;
    background:
      radial-gradient(circle at 30% 20%, rgba(255,255,255,.75), transparent 45%),
      linear-gradient(180deg, var(--sky-mid) 0%, var(--sky-top) 38%, var(--sky-mid) 75%, var(--sky-deep) 100%);
  }
  .garment-art {
    position: absolute; right: 0; top: 600px; width: 440px; height: 430px;
    border-radius: 220px 0 0 60px;
    background:
      radial-gradient(circle at 20% 70%, rgba(246,150,190,.55), transparent 30%),
      radial-gradient(ellipse at 55% 45%, #ffffff 0%, #e3f3fc 40%, rgba(120,200,240,.2) 75%, transparent 100%);
  }
  .fibre-zoom {
    position: absolute; right: 48px; bottom: 80px; width: 150px; height: 150px;
    border-radius: 50%; border: 6px solid #e8eef3;
    background: linear-gradient(160deg, #bfe4f8 0%, #ffffff 60%, #dfe9f0 100%);
  }

  .label-copy {
    position: absolute; left: 66px; top: 370px;
    display: flex; flex-direction: column; align-items: flex-start;
  }
  .brand {
    display: flex; align-items: center; gap: 14px;
    font-weight: 800; font-size: 76px; line-height: 1; color: var(--purple); letter-spacing: -1px;
  }
  .brand-dot { width: 26px; height: 26px; border-radius: 50%; background: var(--purple); }

  .range {
    margin: 22px 0 4px 70px;
    font-family: "Alfa Slab One", serif; font-size: 28px; line-height: 1.1; color: var(--ink); letter-spacing: 1px;
  }
  .product { font-family: "Alfa Slab One", serif; font-weight: 400; }
  .product-main { display: block; font-size: 128px; line-height: .95; color: var(--navy); }
  .product-sub { display: block; font-size: 71px; line-height: 1; color: var(--magenta); margin-top: 4px; }
  .scent {
    margin-top: 14px;
    font-family: "Grenze", serif; font-weight: 600; font-size: 40px; line-height: 1.2; color: var(--ink);
  }

  .benefits { margin-top: 8px; list-style: none; font-size: 26px; color: var(--ink); line-height: 1.45; }
  .benefits li { display: flex; align-items: center; gap: 14px; }
  .benefits svg { width: 22px; height: 22px; flex: none; }

  .claim {
    margin: 20px 0 0 -66px; width: 260px; height: 46px; padding-left: 60px;
    background: var(--magenta); color: var(--white);
    font-family: "Oswald", sans-serif; font-weight: 500; font-size: 27px; line-height: 46px;
    clip-path: polygon(0 0, 100% 0, 92% 50%, 100% 100%, 0 100%);
  }
  .power {
    margin: 8px 0 0 4px; display: flex; align-items: center; gap: 6px;
    color: var(--magenta); font-family: "Baloo 2", sans-serif; font-weight: 800;
  }
  .power-big { font-size: 72px; line-height: 1; }
  .power-small { font-size: 30px; line-height: .85; }

  .guarantee-seal {
    position: absolute; left: 340px; top: 910px; width: 120px; height: 120px; border-radius: 50%;
    background: radial-gradient(circle, #f7d86a 0%, var(--gold) 55%, var(--gold-deep) 100%);
  }
</style>
</head>
<body>
  <section class="label">
    <div class="label-backdrop" role="img" aria-label="Soft blue water backdrop with floating bubbles"></div>
    <div class="garment-art" role="img" aria-label="Fresh white shirt swirling in water with pink petals"></div>
    <div class="fibre-zoom" role="img" aria-label="Magnified close-up of soft fabric fibres"></div>

    <div class="label-copy">
      <div class="brand"><span class="brand-dot"></span>Lumera</div>
      <div class="range">ULTRA</div>
      <h1 class="product"><span class="product-main">Fabric</span><span class="product-sub">SOFTENER</span></h1>
      <div class="scent">Exotic Flowers</div>

      <ul class="benefits">
        <li><svg viewBox="0 0 24 24"><rect x="2" y="3" width="18" height="18" fill="none" stroke="#2c2a55" stroke-width="2"/><path d="M6 12l4 4 11-12" fill="none" stroke="#2c2a55" stroke-width="2.5"/></svg>Fresh and Clean</li>
        <li><svg viewBox="0 0 24 24"><rect x="2" y="3" width="18" height="18" fill="none" stroke="#2c2a55" stroke-width="2"/><path d="M6 12l4 4 11-12" fill="none" stroke="#2c2a55" stroke-width="2.5"/></svg>Dermatologist Tested</li>
        <li><svg viewBox="0 0 24 24"><rect x="2" y="3" width="18" height="18" fill="none" stroke="#2c2a55" stroke-width="2"/><path d="M6 12l4 4 11-12" fill="none" stroke="#2c2a55" stroke-width="2.5"/></svg>Smart green know how</li>
      </ul>

      <div class="claim">Kills 99.99%</div>
      <div class="power"><span class="power-big">2X</span><span class="power-small">More<br>Power</span></div>
    </div>

    <div class="guarantee-seal" role="img" aria-label="Satisfaction guarantee seal"></div>
  </section>
</body>
</html>
```